Patent Law

Need to develop a home page for a patent lawyer.

Colors should go with logo, blues...

Company Name- Velric Dunmore, PLLC

Company Overview-

I am an Intellectual Property Lawyer and focus on patents, copyrights, trademarks, & trade secrets. I work with small businesses and start ups in the chemical and biotech industries.

Why Us-

I am small firm that can provide large-firm service at a reasonable price. I also can charge flat-fees for entreprenuers in certain practice areas.

Services-
Intellectual Property
Patents
Copyrights
Trademarks
Trade secrets
Healthcare Compliance
Elder law
Wills
Trusts

Website we like-
http://www.tolvanecrest.com/ - within industry!!
http://www.quarnhollet.com/
http://brevicktallon.com/
http://thegravelwrights.com/

Target Market(s)

My customers will be small business, specifically small start-up companies in the chemical and biotech arena.

Industry/Entity Type

Trade

Requirements
Must have
• Colors should go with logo, blues...

```html
<!DOCTYPE html>
<html lang="en">
<head>
<meta charset="utf-8">
<title>Velric Dunmore, PLLC</title>
<link href="https://fonts.googleapis.com/css2?family=Arimo:wght@400;700&display=swap" rel="stylesheet">
<style>
:root{
  --blue:#0b7fc4;
  --blue-dark:#1a5fa8;
  --ink:#333;
  --text:#444;
  --muted:#777;
  --line:#ddd;
  --band:#e6e6e6;
  --footer:#222;
  --white:#fff;
}
*{margin:0;padding:0;box-sizing:border-box}
html,body{width:1200px;height:1030px;overflow:hidden;background:var(--white)}
body{position:relative;font-family:"Arimo",Arial,sans-serif;color:var(--text)}
.abs{position:absolute}

/* header */
.brand{left:128px;top:40px;display:flex;align-items:center;gap:10px}
.brand-mark{width:34px;height:34px;border-radius:50%;background:var(--blue)}
.brand-name{font-size:17px;color:var(--blue-dark);letter-spacing:.5px;font-weight:400}
.topbar{right:124px;top:20px;display:flex;align-items:center;font-size:12.5px;color:var(--ink)}
.topbar .phone-icon{width:22px;height:22px;border-radius:50%;border:1px solid var(--line);display:flex;align-items:center;justify-content:center;margin-right:10px}
.topbar .sep{width:1px;height:16px;background:var(--line);margin:0 12px 0 8px}
.topbar .pin{margin-right:8px}
.main-nav{right:123px;top:68px;display:flex;align-items:center;font-size:12.5px;color:var(--ink)}
.main-nav a{color:inherit;text-decoration:none;padding:0 17px;position:relative}
.main-nav a+a::before{content:"";position:absolute;left:0;top:1px;height:12px;width:1px;background:var(--line)}
.main-nav a.active{border:2px solid #6cb4e0;padding:5px 9px;margin-right:2px}
.main-nav a.active+a::before{display:none}
.main-nav a:last-child{padding-right:0}

/* hero */
.hero-band{left:0;top:119px;width:1200px;height:379px;background:var(--band)}
.hero-photo{left:125px;top:119px;width:950px;height:379px;
  background:linear-gradient(180deg,#c9d8e0 0%,#e8eef0 30%,#b8c7d3 60%,#8fa6bd 100%)}
.hero-arrow{width:24px;height:24px;top:321px}
.hero-caption{left:175px;top:390px;width:492px;height:72px;background:var(--white);
  border:1px solid var(--blue);border-left-width:2px;padding:17px 8px;
  color:var(--blue);font-weight:700;font-size:18px;line-height:22px}

/* cards */
.card{top:557px;width:302px;height:357px;border:2px solid #e3e3e3;border-radius:5px;
  background:var(--white);box-shadow:0 3px 0 #e0e0e0}
.card-icon{top:522px;width:92px;height:79px;border:3px solid #d8d8d8;border-radius:3px;background:var(--blue);
  display:flex;align-items:center;justify-content:center}
.card-title{top:618px;width:302px;text-align:center;font-size:24px;color:var(--ink);font-weight:400}
.card-sub{top:644px;width:302px;text-align:center;font-size:11px;color:var(--ink)}
.rule{height:0;border-top:1px dotted #555}
.why-text{left:144px;top:677px;width:264px;font-size:12.3px;line-height:22px;text-align:justify;color:var(--text)}
.read-more{left:330px;top:883px;font-size:12.5px;color:var(--ink);display:flex;align-items:center;gap:9px}
.service{left:467px;width:262px;font-size:12.3px;color:var(--ink);display:flex;align-items:center;gap:12px}
.contact-line{left:826px;font-size:12.3px;color:var(--ink);line-height:22px}
.search-box{left:826px;top:864px;width:224px;height:36px;border:2px solid #e6e6e6;border-radius:5px}

/* footer */
.footer{left:126px;top:945px;width:949px;height:85px;background:var(--footer)}
.footer-nav{left:145px;top:969px;font-size:12.5px;color:#eee}
.footer-nav span{margin:0 6px;color:#bbb}
.copyright{left:141px;top:1000px;font-size:12.5px;color:#eee}
.newsletter{left:527px;top:979px;width:266px;height:36px;border:2px solid #eee;background:var(--white);display:flex}
.newsletter .field{flex:1;font-size:12.5px;color:#555;padding:9px 16px;letter-spacing:.3px}
.newsletter .go{width:50px;background:var(--blue);display:flex;align-items:center;justify-content:center}
.social{top:978px;width:32px;height:32px;border-radius:50%;background:#555}
</style>
</head>
<body>

<header>
  <div class="abs brand"><span class="brand-mark"></span><span class="brand-name">VELRIC DUNMORE, PLLC</span></div>
  <div class="abs topbar">
    <span class="phone-icon"><svg width="10" height="8" viewBox="0 0 10 8"><path d="M1 3c2-2 6-2 8 0v2H7V3.5H3V5H1z M3 4h4l1 3H2z" fill="#0b7fc4"/></svg></span>
    877-402-5190
    <span class="sep"></span>
    <svg class="pin" width="12" height="18" viewBox="0 0 12 18"><path d="M6 0a6 6 0 0 1 6 6c0 4-6 12-6 12S0 10 0 6a6 6 0 0 1 6-6z" fill="#3aa7dd"/><circle cx="6" cy="6" r="2.2" fill="#fff"/></svg>
    Map
  </div>
  <nav class="abs main-nav">
    <a class="active" href="#">Home</a><a href="#">About Us</a><a href="#">Services</a><a href="#">Careers</a><a href="#">News</a><a href="#">Contact</a>
  </nav>
</header>

<section>
  <div class="abs hero-band"></div>
  <div class="abs hero-photo" role="img" aria-label="Photo of a team of business professionals standing together in a bright office"></div>
  <svg class="abs hero-arrow" style="left:150px" viewBox="0 0 24 24"><circle cx="12" cy="12" r="11" fill="#fff" stroke="#0b7fc4" stroke-width="1.5"/><path d="M14 7l-5 5 5 5z" fill="#0b7fc4"/></svg>
  <svg class="abs hero-arrow" style="left:1023px" viewBox="0 0 24 24"><circle cx="12" cy="12" r="11" fill="#fff" stroke="#0b7fc4" stroke-width="1.5"/><path d="M10 7l5 5-5 5z" fill="#0b7fc4"/></svg>
  <div class="abs hero-caption">Real people with real world answers &amp; solutions to help move your business forward.</div>
</section>

<main>
  <!-- why us -->
  <div class="abs card" style="left:125px"></div>
  <div class="abs card-icon" style="left:234px"><svg width="54" height="44" viewBox="0 0 54 44"><path d="M4 24l14 14L50 6" fill="none" stroke="#fff" stroke-width="8"/></svg></div>
  <h2 class="abs card-title" style="left:135px">WHY US</h2>
  <div class="abs rule" style="left:145px;top:662px;width:260px"></div>
  <p class="abs why-text">Donec nec justo eget felis facilisis fermentum. Aliquam porttitor mauris sit amet orci. Aenean dignissim pellentesque felis.Donec nec justo eget felis facilisis fermentum. Aliquam porttitor mauris sit amet orci. Aenean dignissim pellentesque felis.Donec nec justo eget felis facilisis fermentum. Aliquam porttitor mauris sit amet orci. Aenean dignissim pellentesque felis.Donec nec justo eget felis facilisis fermentum. Aliquam</p>
  <div class="abs read-more"><svg width="8" height="10" viewBox="0 0 8 10"><path d="M0 0l8 5-8 5z" fill="#0b7fc4"/></svg>Read More</div>

  <!-- what we do -->
  <div class="abs card" style="left:449px"></div>
  <div class="abs card-icon" style="left:558px"><svg width="66" height="58" viewBox="0 0 66 58"><rect x="3" y="3" width="60" height="52" fill="none" stroke="#fff" stroke-width="5"/><path d="M33 12v34M16 29h34" stroke="#fff" stroke-width="6"/></svg></div>
  <h2 class="abs card-title" style="left:455px">WHAT WE DO</h2>
  <div class="abs card-sub" style="left:452px">( list of services )</div>
  <div class="abs rule" style="left:469px;top:662px;width:260px"></div>
  <div class="abs service" style="top:681px"><svg width="15" height="15" viewBox="0 0 15 15"><circle cx="7.5" cy="7.5" r="6.5" fill="none" stroke="#0b7fc4" stroke-width="1.3"/><path d="M4.5 7.5l2 2 4-4" fill="none" stroke="#0b7fc4" stroke-width="1.5"/></svg>Intellectual Property</div>
  <div class="abs rule" style="left:469px;top:710px;width:260px"></div>
  <div class="abs service" style="top:723px"><svg width="15" height="15" viewBox="0 0 15 15"><circle cx="7.5" cy="7.5" r="6.5" fill="none" stroke="#0b7fc4" stroke-width="1.3"/><path d="M4.5 7.5l2 2 4-4" fill="none" stroke="#0b7fc4" stroke-width="1.5"/></svg>Patents</div>
  <div class="abs rule" style="left:469px;top:752px;width:260px"></div>
  <div class="abs service" style="top:766px"><svg width="15" height="15" viewBox="0 0 15 15"><circle cx="7.5" cy="7.5" r="6.5" fill="none" stroke="#0b7fc4" stroke-width="1.3"/><path d="M4.5 7.5l2 2 4-4" fill="none" stroke="#0b7fc4" stroke-width="1.5"/></svg>Copyrights</div>
  <div class="abs rule" style="left:469px;top:794px;width:260px"></div>
  <div class="abs service" style="top:807px"><svg width="15" height="15" viewBox="0 0 15 15"><circle cx="7.5" cy="7.5" r="6.5" fill="none" stroke="#0b7fc4" stroke-width="1.3"/><path d="M4.5 7.5l2 2 4-4" fill="none" stroke="#0b7fc4" stroke-width="1.5"/></svg>Healthcare Compliance</div>
  <div class="abs rule" style="left:469px;top:835px;width:260px"></div>
  <div class="abs service" style="top:849px"><svg width="15" height="15" viewBox="0 0 15 15"><circle cx="7.5" cy="7.5" r="6.5" fill="none" stroke="#0b7fc4" stroke-width="1.3"/><path d="M4.5 7.5l2 2 4-4" fill="none" stroke="#0b7fc4" stroke-width="1.5"/></svg>Trade secrets</div>
  <div class="abs rule" style="left:469px;top:876px;width:260px"></div>
  <div class="abs service" style="top:886px"><svg width="15" height="15" viewBox="0 0 15 15"><circle cx="7.5" cy="7.5" r="6.5" fill="none" stroke="#0b7fc4" stroke-width="1.3"/><path d="M4.5 7.5l2 2 4-4" fill="none" stroke="#0b7fc4" stroke-width="1.5"/></svg>Trademarks</div>

  <!-- contact info -->
  <div class="abs card" style="left:773px"></div>
  <div class="abs card-icon" style="left:882px"><svg width="76" height="50" viewBox="0 0 76 50"><path d="M6 22c0-12 14-20 24-16l-3 7c-6-2-12 2-12 8z" fill="#fff"/><rect x="22" y="14" width="52" height="34" fill="#fff"/><path d="M22 14l26 20 26-20" fill="none" stroke="#0b7fc4" stroke-width="4"/></svg></div>
  <h2 class="abs card-title" style="left:778px">CONTACT INFO</h2>
  <div class="abs rule" style="left:793px;top:662px;width:260px"></div>
  <svg class="abs" style="left:794px;top:679px" width="20" height="28" viewBox="0 0 20 28"><path d="M10 0a10 10 0 0 1 10 10c0 7-10 18-10 18S0 17 0 10A10 10 0 0 1 10 0z" fill="#111"/><circle cx="10" cy="10" r="4" fill="#fff"/></svg>
  <p class="abs contact-line" style="top:675px">123 Example Way<br>San Francisco, CA 94108<br>USA</p>
  <svg class="abs" style="left:794px;top:769px" width="14" height="14" viewBox="0 0 14 14"><path d="M3 1l3 3-2 2c1 2 2 3 4 4l2-2 3 3-2 2C5 13 1 9 1 3z" fill="#111"/></svg>
  <p class="abs contact-line" style="top:761px">(123) 123 - 4566 - 000<br>(123) 536 - 7472 - 000</p>
  <svg class="abs" style="left:795px;top:823px" width="16" height="12" viewBox="0 0 16 12"><rect x="1" y="1" width="14" height="10" fill="none" stroke="#111" stroke-width="1.6"/><path d="M1 1l7 6 7-6" fill="none" stroke="#111" stroke-width="1.6"/></svg>
  <p class="abs contact-line" style="top:816px">contact@velricdunmore.com<br>info@velricdunmore.com</p>
  <svg class="abs" style="left:794px;top:876px" width="18" height="18" viewBox="0 0 18 18"><circle cx="11" cy="7" r="5" fill="none" stroke="#111" stroke-width="2"/><path d="M7 11l-5 5" stroke="#111" stroke-width="3"/></svg>
  <div class="abs search-box"></div>
</main>

<footer>
  <div class="abs footer"></div>
  <div class="abs footer-nav">Home<span>|</span>Pages<span>|</span>Blog<span>|</span>Shortcodes<span>|</span>Features<span>|</span>Contact</div>
  <div class="abs copyright">© 2013 Velric Dunmore. All rights reserved.</div>
  <div class="abs newsletter"><span class="field">NEWSLETTER</span><span class="go"><svg width="24" height="22" viewBox="0 0 24 22"><circle cx="10" cy="10" r="7" fill="none" stroke="#fff" stroke-width="3"/><path d="M15 15l6 5" stroke="#fff" stroke-width="3"/></svg></span></div>
  <span class="abs social" style="left:849px"></span>
  <span class="abs social" style="left:890px"></span>
  <span class="abs social" style="left:933px"></span>
  <span class="abs social" style="left:974px"></span>
  <span class="abs social" style="left:1017px"></span>
</footer>

</body>
</html>
```